quarry productions business cards design

design a clean look but creative business card for a production company, I'm a freelance producer and launching my startup, would like to keep a clean professional look but still creative

Target Market(s)

businesses

Industry/Entity Type

video production

Contact Information for Business Card

logo, name (Karl Benn), Title (Producer), (MFA Filmmaking, QTSA Los Angeles), contact number & email ID

Colors

Designer to choose only greyscale colors for use in the design.

Requirements
Must have
• logo, black and white colors, you can play with their shades
Nice to have
• a unique design, not necessarily a typical size card
Should not have
• too colorful or playful

```html
<!DOCTYPE html>
<html lang="en">
<head>
<meta charset="utf-8">
<title>Quarry Productions — Business Cards</title>
<link rel="stylesheet" href="https://fonts.googleapis.com/css2?family=Inter:wght@400;600;700&display=swap">
<style>
  :root {
    --backdrop: #979797;
    --card: #262424;
    --ink: #ffffff;
    --ink-soft: #e9e9e9;
  }
  * { margin: 0; padding: 0; box-sizing: border-box; }
  html, body {
    width: 1200px; height: 1200px; overflow: hidden;
    background: var(--backdrop);
    font-family: "Inter", Arial, sans-serif;
    color: var(--ink);
  }
  .card {
    position: absolute;
    left: 262px;
    width: 686px;
    height: 392px;
    background: var(--card);
  }
  .card--front { top: 165px; }
  .card--back { top: 653px; }

  .identity {
    position: absolute; top: 112px; left: 0; right: 0;
    text-align: center;
  }
  .identity__name {
    font-weight: 600; font-size: 24px; letter-spacing: 0.3px; line-height: 1.1;
  }
  .identity__title {
    font-weight: 400; font-size: 16px; color: var(--ink-soft); margin-top: 2px;
  }

  .details {
    position: absolute; top: 184px; left: 0; right: 0;
    font-size: 16px; line-height: 20px; color: var(--ink-soft);
  }
  .details__credentials {
    position: absolute; right: 363px; text-align: right; white-space: nowrap;
  }
  .details__divider {
    position: absolute; left: 337px; top: 6px; width: 1px; height: 32px;
    background: var(--ink-soft);
  }
  .details__contact {
    position: absolute; left: 348px; white-space: nowrap; top: 2px;
  }
  .contact-line { display: flex; align-items: center; gap: 8px; }
  .contact-line svg { width: 12px; height: 12px; fill: var(--ink); }

  .website {
    position: absolute; top: 254px; left: 0; right: 0;
    text-align: center; font-size: 16px; color: var(--ink-soft);
  }

  .wordmark {
    position: absolute; top: 50%; left: 50%;
    transform: translate(-50%, -50%);
    display: flex; align-items: center; gap: 16px;
  }
  .wordmark__mark {
    width: 22px; height: 22px; background: var(--ink);
  }
  .wordmark__name {
    font-weight: 600; font-size: 28px; line-height: 1.05; letter-spacing: 0.5px;
    text-transform: uppercase;
  }
</style>
</head>
<body>
  <section class="card card--front">
    <div class="identity">
      <h1 class="identity__name">KARL BENN</h1>
      <p class="identity__title">Producer</p>
    </div>
    <div class="details">
      <div class="details__credentials">
        <p>MFA Filmmaking</p>
        <p>QTSA Los Angeles</p>
      </div>
      <span class="details__divider"></span>
      <div class="details__contact">
        <p class="contact-line">
          <svg viewBox="0 0 24 24" aria-hidden="true"><path d="M6.6 10.8a15.1 15.1 0 0 0 6.6 6.6l2.2-2.2a1 1 0 0 1 1-.25 11.4 11.4 0 0 0 3.6.57 1 1 0 0 1 1 1V20a1 1 0 0 1-1 1A17 17 0 0 1 3 4a1 1 0 0 1 1-1h3.5a1 1 0 0 1 1 1c0 1.25.2 2.45.57 3.57a1 1 0 0 1-.25 1z"/></svg>
          <span>555-014-2291</span>
        </p>
        <p class="contact-line">
          <svg viewBox="0 0 24 24" aria-hidden="true"><path d="M2 5h20v14H2z M3.5 6.5 12 13l8.5-6.5" /></svg>
          <span>info@quarryfilms.com</span>
        </p>
      </div>
    </div>
    <p class="website">www.Quarryfilms.com</p>
  </section>

  <section class="card card--back">
    <div class="wordmark">
      <span class="wordmark__mark"></span>
      <p class="wordmark__name">Quarry<br>Productions</p>
    </div>
  </section>
</body>
</html>
```